QZN Supplements needs a label designer for supplement company

Looking for an on going label designer for my supplement company. I have three products that will need designs. I'm about to launch my sleep supplement called Velmora Rest and that's the first design needed.
I would like all designs to be somewhat simple, not overstated and uniformed so that when you look at all of the labels of the different supplements they are similar and you can tell it's the same brand.
Please see attached sample pictures below as ideas.
Updates

The brand is QZN supplements, logo file has been provided. The supplement is called Velmora Rest. It is a liquid supplement that is a 32/33 ounce white bottle. Die lines and measurements will be provided. Here's text for wording ideas: Wording: Natural Sleep Aid Reset your circadian rhythm. May help you: Fall asleep faster. Get a deeper more restful sleep. Boost Immune System Remember your dreams. Protect your brain and flush toxins. Wake up feeling refreshed. Non-gmo Gluten Free Sugar Free Vegan Manufactured in cGMP factory Manufactured in USA

Target Market(s)

Health and wellness/supplement industry for regular people not hardcore gym goers. My supplements are for a health lifestyle not bodybuilding.

Industry/Entity Type

Health And Wellness

Colors
3176b5
3276b5
33a6d7
85cae6
85abd2
cedeed
e4daeb
b7a5cd

Requirements
Must have
• There will be some text and wording that I will provide that must be on the bottles.

```html
<!DOCTYPE html>
<html lang="en">
<head>
<meta charset="utf-8">
<title>Velmora Rest Label – QZN Supplements</title>
<link rel="stylesheet" href="https://fonts.googleapis.com/css2?family=Roboto+Condensed:wght@400;700&display=swap">
<style>
  :root {
    --canvas-bg: #ebebeb;
    --label-purple: #6245a8;
    --label-purple-light: #7c60bf;
    --label-purple-dark: #553a98;
    --label-white: #ffffff;
    --label-lavender: #cdbdec;
  }
  html, body {
    margin: 0;
    padding: 0;
    width: 1200px;
    height: 900px;
    overflow: hidden;
    background: var(--canvas-bg);
  }
  .canvas {
    position: relative;
    width: 1200px;
    height: 900px;
    background: var(--canvas-bg);
  }
  .label {
    position: absolute;
    left: 312px;
    top: 37px;
    width: 575px;
    height: 825px;
    background: linear-gradient(90deg,
      var(--label-purple-light) 0%,
      var(--label-purple) 30%,
      var(--label-purple-dark) 55%,
      var(--label-purple) 80%,
      var(--label-purple-light) 100%);
    font-family: "Roboto Condensed", "Arial Narrow", sans-serif;
    color: var(--label-white);
  }
  .brand {
    position: absolute;
    left: 95px;
    top: 48px;
    display: flex;
    align-items: center;
    gap: 22px;
  }
  .brand-mark {
    width: 60px;
    height: 60px;
    border-radius: 50%;
    border: 4px solid var(--label-white);
    box-sizing: border-box;
  }
  .brand-name {
    font-weight: 700;
    font-size: 32px;
    letter-spacing: 0.5px;
    text-transform: uppercase;
  }
  .product-art {
    position: absolute;
    left: 122px;
    top: 138px;
    width: 330px;
    height: 240px;
    border-radius: 48% 52% 45% 40% / 50% 55% 45% 50%;
    background: radial-gradient(ellipse at 45% 45%, rgba(255,255,255,0.95) 0%, rgba(240,236,250,0.85) 55%, rgba(220,210,240,0.55) 100%);
  }
  .product-name {
    position: absolute;
    left: 100px;
    top: 400px;
    margin: 0;
    font-weight: 700;
    font-size: 52px;
    line-height: 1;
    letter-spacing: 2px;
    text-transform: uppercase;
  }
  .product-type {
    position: absolute;
    left: 275px;
    top: 466px;
    margin: 0;
    font-weight: 700;
    font-size: 42px;
    line-height: 1;
    letter-spacing: 26px;
    text-transform: uppercase;
  }
  .tagline {
    position: absolute;
    left: 0;
    right: 0;
    top: 534px;
    margin: 0;
    text-align: center;
    font-weight: 700;
    font-size: 18px;
    letter-spacing: 0.5px;
    text-transform: uppercase;
    color: var(--label-lavender);
  }
  .benefits {
    position: absolute;
    left: 70px;
    right: 50px;
    top: 566px;
    font-size: 15px;
    line-height: 1.35;
  }
  .benefits-intro {
    margin: 0 0 4px;
    font-weight: 700;
  }
  .benefits-list {
    margin: 0;
    padding: 0;
    list-style: none;
    display: grid;
    grid-template-columns: 1fr 1fr;
    column-gap: 18px;
  }
  .benefits-list li::before {
    content: "✓ ";
    color: var(--label-lavender);
    font-weight: 700;
  }
  .claims {
    position: absolute;
    left: 0;
    right: 0;
    top: 680px;
    margin: 0;
    text-align: center;
    font-weight: 700;
    font-size: 16px;
    letter-spacing: 1px;
    text-transform: uppercase;
  }
  .product-format {
    position: absolute;
    left: 0;
    right: 0;
    top: 722px;
    margin: 0;
    text-align: center;
    font-weight: 700;
    font-size: 24px;
    letter-spacing: 0.3px;
    text-transform: uppercase;
    color: var(--label-lavender);
  }
  .origin {
    position: absolute;
    left: 0;
    right: 0;
    top: 766px;
    margin: 0;
    text-align: center;
    font-size: 14px;
    letter-spacing: 0.3px;
  }
</style>
</head>
<body>
  <main class="canvas">
    <section class="label">
      <div class="brand">
        <span class="brand-mark"></span>
        <span class="brand-name">QZN Supplements</span>
      </div>
      <div class="product-art" role="img" aria-label="Stylised white brain emblem illustration"></div>
      <h1 class="product-name">Velmora</h1>
      <p class="product-type">Rest</p>
      <p class="tagline">Natural Sleep Aid · Reset your circadian rhythm</p>
      <div class="benefits">
        <p class="benefits-intro">May help you:</p>
        <ul class="benefits-list">
          <li>Fall asleep faster</li>
          <li>Get a deeper, more restful sleep</li>
          <li>Boost immune system</li>
          <li>Remember your dreams</li>
          <li>Protect your brain &amp; flush toxins</li>
          <li>Wake up feeling refreshed</li>
        </ul>
      </div>
      <p class="claims">Non-GMO · Gluten Free · Sugar Free · Vegan</p>
      <p class="product-format">Liquid Dietary Supplement - 32 FL OZ</p>
      <p class="origin">Manufactured in USA in a cGMP factory</p>
    </section>
  </main>
</body>
</html>
```